Land Buying Company Needs Letterhead for Direct Mail Marketing to Land Owners

We are looking for a professional letterhead that we will be including in our direct mail marketing. We will be sending this to land owners who may be interested in selling or purchasing land.

The letterhead needs to be editable. Headers and footers would look nice, but we are open. We would want it to include our address, website, phone, and email info. For right now the address to use for design purposes would the following:

Address: 415 Bramwell Avenue #600
Dallas, TX 75219
Website - www.quillridgeacres.example
Email - info@quillridgeacres.example
Phone - 866-402-ACRE

I have attached our logo zip file that we just had done on Pixel Guild. Let me know what questions you have, and thank you.

```html
<!DOCTYPE html>
<html lang="en">
<head>
<meta charset="utf-8">
<title>Quill Ridge Acres – Letterhead</title>
<link rel="stylesheet" href="https://fonts.googleapis.com/css2?family=Montserrat:wght@700&family=Open+Sans:wght@400&family=Roboto:wght@400&display=swap">
<style>
  :root {
    --backdrop: #e2e2e2;
    --paper: #fafafa;
    --forest: #4a6b2a;
    --leaf: #8dc63f;
    --ink-dark: #2f2f2f;
    --ink-body: #8a8a8a;
    --watermark: #efefec;
    --signature-tone: #ececec;
  }
  * { margin: 0; padding: 0; box-sizing: border-box; }
  html, body {
    width: 1200px; height: 800px; overflow: hidden;
    background: var(--backdrop);
  }
  .letterhead {
    position: absolute; left: 330px; top: 20px;
    width: 540px; height: 760px;
    background: var(--paper);
    overflow: hidden;
  }
  .brand {
    position: absolute; left: 39px; top: 74px;
    display: flex; align-items: center; gap: 9px;
  }
  .brand-dot {
    width: 32px; height: 32px; border-radius: 50%;
    background: var(--forest);
  }
  .brand-name {
    font-family: "Montserrat", sans-serif; font-weight: 700;
    font-size: 19px; letter-spacing: 0.5px;
    color: var(--leaf); text-transform: uppercase;
  }
  .contact {
    position: absolute; left: 329px; top: 64px;
    font-family: "Roboto", sans-serif; font-size: 10px; line-height: 13.2px;
    color: var(--ink-dark);
    list-style: none;
  }
  .contact li { display: flex; align-items: center; gap: 3px; }
  .contact svg { width: 8px; height: 8px; fill: var(--ink-dark); }
  .watermark {
    position: absolute; left: 109px; top: 219px;
    width: 320px; height: 320px; border-radius: 50%;
    background: var(--watermark);
  }
  .letter-body {
    position: absolute; left: 49px; top: 198px; width: 441px;
    font-family: "Open Sans", sans-serif; font-size: 9.9px; line-height: 14.7px;
    color: var(--ink-body);
  }
  .letter-body p { margin-bottom: 14.5px; text-align: justify; }
  .letter-body .salutation, .letter-body .closing { text-align: left; }
  .signature {
    position: absolute; left: 49px; top: 582px;
    width: 64px; height: 60px; background: var(--signature-tone);
  }
  .footer-band {
    position: absolute; left: 0; bottom: 1px; width: 100%; height: 8px;
    background: var(--leaf);
  }
  .footer-url {
    position: absolute; right: 6px; bottom: 1px;
    width: 204px; height: 20px;
    background: var(--forest);
    clip-path: polygon(12px 0, 100% 0, 100% 100%, 0 100%);
    font-family: "Roboto", sans-serif; font-size: 10px; color: #fff;
    display: flex; align-items: center; justify-content: center; padding-left: 6px;
  }
</style>
</head>
<body>
  <main class="letterhead">
    <header>
      <div class="brand">
        <span class="brand-dot"></span>
        <span class="brand-name">Quill Ridge Acres</span>
      </div>
      <ul class="contact">
        <li>415 Bramwell Avenue #600</li>
        <li>Dallas, TX 75219</li>
        <li><svg viewBox="0 0 10 10" aria-hidden="true"><path d="M1 3.5C1 2 2.5 1 5 1s4 1 4 2.5L7.6 4.3 7 3.2H3L2.4 4.3ZM2.5 5h5l1 4h-7Z"/></svg>866-402-ACRE</li>
        <li><svg viewBox="0 0 10 10" aria-hidden="true"><path d="M0.5 2h9v6.5h-9Zm1 1 3.5 2.6L8.5 3Z"/></svg>info@quillridgeacres.example</li>
      </ul>
    </header>

    <div class="watermark" aria-hidden="true"></div>

    <article class="letter-body">
      <p class="salutation">Dear customer,</p>
      <p>Lorem ipsum dolor sit amet, consectetur adipisicing elit, sed do eiusmod tempor incididunt ut labore et dolore magna aliqua. Ut enim ad minim veniam, quis nostrud exercitation ullamco laboris nisi ut aliquip ex ea commodo consequat. Duis aute irure dolor in reprehenderit in voluptate velit esse cillum dolore eu fugiat nulla pariatur. Excepteur sint occaecat cupidatat non proident, sunt in culpa qui officia deserunt mollit anim id est laborum.</p>
      <p>Lorem ipsum dolor sit amet, consectetur adipisicing elit, sed do eiusmod tempor incididunt ut labore et dolore magna aliqua. Ut enim ad minim veniam, quis nostrud exercitation ullamco laboris nisi ut aliquip ex ea commodo consequat. Duis aute irure dolor in reprehenderit in voluptate velit esse cillum dolore eu fugiat nulla pariatur. Excepteur sint occaecat cupidatat non proident, sunt in culpa qui officia deserunt mollit anim id est laborum.</p>
      <p>Lorem ipsum dolor sit amet, consectetur adipisicing elit, sed do eiusmod tempor incididunt ut labore et dolore magna aliqua. Ut enim ad minim veniam, quis nostrud exercitation ullamco laboris nisi ut aliquip ex ea commodo consequat. Duis aute irure dolor in reprehenderit in voluptate velit esse cillum dolore eu fugiat nulla pariatur. Excepteur sint occaecat cupidatat non proident, sunt in culpa qui officia deserunt mollit anim id est laborum.</p>
      <p>Lorem ipsum dolor sit amet, consectetur adipisicing elit, sed do eiusmod tempor incididunt ut labore et dolore magna aliqua. Ut enim ad minim veniam, quis nostrud exercitation ullamco laboris nisi ut aliquip ex ea commodo consequat. Duis aute irure dolor in reprehenderit.</p>
      <p class="closing">Yours Sincerely,</p>
    </article>

    <div class="signature" role="img" aria-label="Handwritten signature of the sender"></div>

    <footer>
      <div class="footer-band"></div>
      <div class="footer-url">www.quillridgeacres.example</div>
    </footer>
  </main>
</body>
</html>
```